Cutting Board Oil Label

I would like a label created for our custom made cutting board oil. The bottle will be clear and come in several different sizes. I have included the current label we use. We would like the information to stay the same, but more aesthetically pleasing and professionally presented. I am also including our logo and the current label of our biggest competitor.

```html
<!DOCTYPE html>
<html lang="en">
<head>
<meta charset="UTF-8">
<title>Cutting Board Conditioner Label</title>
<link href="https://fonts.googleapis.com/css2?family=Montserrat:wght@400;500;600;700&family=Libre+Baskerville:wght@400;700&display=swap" rel="stylesheet">
<style>
  :root {
    --backdrop: #323234;
    --paper: #ffffff;
    --ink: #2b2b2d;
    --charcoal: #333335;
    --sand: #efd39d;
    --teal: #2bbcc7;
    --slate: #6d6e71;
    --white: #ffffff;
  }
  * { margin: 0; padding: 0; box-sizing: border-box; }
  html, body {
    width: 1200px;
    height: 800px;
    overflow: hidden;
    background: var(--backdrop);
  }
  .label {
    position: absolute;
    left: 100px;
    top: 18px;
    width: 1000px;
    height: 764px;
    background: var(--paper);
    font-family: "Montserrat", sans-serif;
    color: var(--ink);
  }
  .brand {
    position: absolute;
    left: 43px;
    width: 504px;
    top: 150px;
    display: flex;
    align-items: center;
    justify-content: center;
    gap: 12px;
  }
  .brand-dot {
    width: 22px;
    height: 22px;
    border-radius: 50%;
    background: var(--teal);
  }
  .brand-name {
    font-family: "Montserrat", sans-serif;
    font-weight: 600;
    font-size: 34px;
    color: var(--slate);
    letter-spacing: 0.5px;
  }
  .title-panel {
    position: absolute;
    left: 43px;
    top: 333px;
    width: 504px;
    height: 199px;
    background: var(--charcoal);
    color: var(--white);
    text-align: center;
  }
  .title-kicker {
    font-family: "Libre Baskerville", serif;
    font-weight: 400;
    font-size: 33px;
    line-height: 1;
    margin-top: 28px;
    letter-spacing: 0.5px;
  }
  .title-main {
    font-family: "Libre Baskerville", serif;
    font-weight: 700;
    font-size: 55px;
    line-height: 1;
    margin-top: 8px;
    letter-spacing: 0.5px;
  }
  .title-uses {
    font-size: 19px;
    line-height: 25px;
    margin-top: 20px;
    letter-spacing: 0.3px;
  }
  .claim-band {
    position: absolute;
    left: 43px;
    top: 532px;
    width: 504px;
    height: 50px;
    background: var(--sand);
    display: flex;
    align-items: center;
    justify-content: center;
    font-weight: 600;
    font-size: 28px;
    letter-spacing: 0.8px;
    color: var(--ink);
  }
  .volume {
    position: absolute;
    left: 43px;
    width: 504px;
    top: 708px;
    text-align: center;
    font-weight: 500;
    font-size: 24px;
  }
  .info {
    position: absolute;
    left: 623px;
    top: 44px;
    width: 341px;
    font-size: 19.5px;
    line-height: 26.6px;
    text-align: justify;
  }
  .info p + p { margin-top: 20px; }
  .info strong { font-weight: 700; }
  .made-in {
    position: absolute;
    left: 623px;
    top: 668px;
    font-weight: 700;
    font-size: 35px;
    color: var(--teal);
    letter-spacing: 0.3px;
  }
  .web {
    position: absolute;
    left: 623px;
    top: 712px;
    font-weight: 700;
    font-size: 20.5px;
    color: var(--ink);
  }
</style>
</head>
<body>
  <main class="label">
    <div class="brand">
      <span class="brand-dot"></span>
      <span class="brand-name">Ridgeline Hollow Goods</span>
    </div>

    <section class="title-panel">
      <h1 class="title-kicker">CUTTING BOARD</h1>
      <h2 class="title-main">CONDITIONER</h2>
      <p class="title-uses">For cutting boards, butcher blocks, wood<br>utensils, and any other wood products.</p>
    </section>
    <div class="claim-band">FOOD SAFE • ALL NATURAL</div>

    <p class="volume">12 fl oz (355 ML)</p>

    <section class="info">
      <p><strong>INGREDIENTS:</strong> Beeswax, Mineral Oil,Orange Oil, Lemon Oil, and Vitamin E</p>
      <p><strong>DIRECTIONS:</strong> Apply a generous amount of conditioner with a clean, lint free cloth. For best results, allow board to soak in conditioner overnight. Using a clean, lint free cloth, buff and remove any excess conditioner. For new or unconditioned cutting boards, butcher blocks, or wooden kitchen utensils we recommend repeating the process a second time to ensure your wood is properly sealed. Recondition about once a month (depending on frequency of use) or when the board begins to become dry to the touch.</p>
    </section>

    <p class="made-in">MADE IN USA</p>
    <p class="web">ridgelinehollowgoods.com</p>
  </main>
</body>
</html>
```